Corporate Website Homepage design

Looking for a design of a Corporate Website, Velkor Pty Ltd. Existing website is quite old, and outdated: www.velkor-example.com.au

Our company has two sides, with consumer facing brands and services for clients to develop their own brands, referred to as Private Label.

Looking for a premium design that incorporates both our services as private label and sourcing specialists, from a corporate side. And also information about our own brands, and a link to a webshop where they can be purchased.

Example General Structure:
Top Menu bar and Logo
Rotating Banner

About Our Services (well presented section of below services, with small descriptions below each one, and space to click through to learn more on each):
- Global Sourcing, Distribution & Supply Solutions
- Specialist Private Label Manufacturing Facilities
- Strict Quality Assurance Processes & Certifications

Brands:
• Pillowpop – Fun & Amazing Value range of baby Clothing, Manchester and Accessories
• Tinamorra – Luxurious Organic Baby Clothing, Wraps and Accessories
• Cradlebloom – Everything Baby at Amazing Prices
• Fenwick Tots – Infant Feeding range with all your favourite Fenwick Characters
• LinenHarbourRange – Luxury range of Towels and Manchester
• KiteTumble – Exciting range of Kids Clothing, with a twist

Product Categories:
Infant Feeding and Accessories
Infant Clothing
Infant Gear
Maternity Wear
Mens Underwear
Homewares and Manchester

Target Market(s)

Corporate Customers - Retailer buyers and Consumers looking for brand information

Industry/Entity Type

Baby

Requirements
Must have
• Good structure split by
Services, Brands and Product to allow people looking for particular things to find them quickly due to different types of visitors (corporate vs consumer)

Clean and Professional Design

with information, should have links to blog, webshop

```html
<!DOCTYPE html>
<html lang="en">
<head>
<meta charset="utf-8">
<title>Velkor International – Home</title>
<link rel="stylesheet" href="https://fonts.googleapis.com/css2?family=Arimo:wght@400;700&family=Black+Ops+One&family=Delius&family=Kaushan+Script&family=Ubuntu:wght@400;500;700&display=swap">
<style>
:root{
  --orange:#f36b0c;
  --orange-light:#fb8a1e;
  --red:#c8102e;
  --maroon:#b01d24;
  --blue:#1d5fa6;
  --blue-link:#1f5d9c;
  --teal:#23c1c0;
  --green:#1fae6f;
  --banner:#f9a516;
  --text:#444;
  --muted:#777;
  --line:#e2e2e2;
  --panel:#f3f3f3;
  --white:#fff;
}
*{box-sizing:border-box;margin:0;padding:0}
html,body{width:814px;height:1200px;overflow:hidden}
body{position:relative;background:var(--white);font-family:Arimo,Arial,sans-serif;color:var(--text);font-size:8px}
.abs{position:absolute}
.top-strip{left:0;top:0;width:814px;height:3px;background:linear-gradient(90deg,#2bb3c0 0 20%,#f39c12 20% 40%,#e5317a 40% 60%,#7ab648 60% 80%,#2f6fb5 80%)}
.logo{left:75px;top:24px;display:flex;align-items:center;gap:6px;font-family:Ubuntu,sans-serif;font-weight:700;font-size:22px;color:var(--blue)}
.logo-dot{width:16px;height:16px;border-radius:50%;background:var(--red)}
.util-links{left:306px;top:22px;font-size:8px;color:var(--muted);word-spacing:2px}
.follow{left:553px;top:19px;font-family:Ubuntu,sans-serif;font-size:13px;color:#333}
.social{top:17px;width:19px;height:19px;border-radius:3px}
.call{left:371px;top:58px;font-family:Ubuntu,sans-serif;font-size:16px;color:#333}
.call span{color:var(--red);font-family:Georgia,serif}
.search{left:573px;top:54px;width:166px;height:30px;border-radius:5px;background:var(--red);padding:3px}
.search-field{width:136px;height:22px;border-radius:4px;background:var(--white);font-size:8px;font-style:italic;color:#aaa;padding:6px 8px}
.search svg{position:absolute;right:9px;top:8px}
.nav{left:0;top:97px;width:814px;height:31px;background:linear-gradient(var(--orange-light),var(--orange));border-bottom:2px dashed #fbc08a}
.nav-home{left:75px;top:97px;width:89px;height:31px;background:#f98a2a}
.nav a{position:absolute;top:9px;color:var(--white);font-family:Ubuntu,sans-serif;font-size:11.5px;text-decoration:none;transform:translateX(-50%)}
.banner-frame{left:74px;top:141px;width:665px;height:272px;border:1px solid #ddd;box-shadow:0 1px 3px rgba(0,0,0,.15);background:var(--white)}
.banner{left:81px;top:149px;width:651px;height:257px;background:var(--banner);overflow:hidden}
.banner-photo{position:absolute;left:215px;top:0;width:436px;height:257px;background:radial-gradient(circle at 50% 40%,#f6d1b4 0,#f3b56c 40%,var(--banner) 75%)}
.banner-script{position:absolute;left:20px;top:16px;font-family:"Kaushan Script",cursive;font-size:40px;color:#ffe31a}
.banner-title{position:absolute;left:20px;top:68px;font-family:Ubuntu,sans-serif;font-size:22px;color:var(--white)}
.banner-text{position:absolute;left:20px;top:106px;width:220px;font-family:Arimo,sans-serif;font-weight:700;font-size:9px;line-height:12px;color:var(--white)}
.btn-shop{position:absolute;left:21px;top:136px;width:85px;height:23px;border-radius:12px;background:var(--teal);color:var(--white);font-family:Ubuntu,sans-serif;font-size:11.5px;text-align:center;line-height:23px}
.dots{position:absolute;left:13px;top:232px;display:flex;gap:3px}
.dots i{width:11px;height:11px;border-radius:50%;background:var(--white)}
.dots i:first-child{background:var(--blue)}
.section-title{font-family:Delius,cursive;font-size:16px;color:var(--maroon)}
.rule{height:2px;background:var(--line)}
.pager{left:503px;top:434px;display:flex;gap:1px}
.pager span{width:15px;height:15px;border:1px solid var(--blue);display:flex;align-items:center;justify-content:center}
.product{top:468px;width:120px;text-align:center;transform:translateX(-50%)}
.product-img{width:84px;height:76px;margin:0 auto;border-radius:10px}
.product h3{margin-top:12px;font-family:Delius,cursive;font-weight:400;font-size:11px;color:var(--maroon)}
.product p{margin-top:3px;font-size:7.2px;line-height:9px;color:var(--muted)}
.add-cart{margin:7px auto 0;width:62px;height:20px;border-radius:4px;background:linear-gradient(#fb8f2b,#ef6a0d);border:2px solid #f8c08c;color:var(--white);font-size:7.5px;line-height:16px;text-align:left;padding-left:5px;position:relative;letter-spacing:-.3px}
.add-cart::after{content:"";position:absolute;right:4px;top:3px;width:8px;height:8px;border-radius:50%;background:var(--white);border:2px solid #bbb}
.cats{left:556px;top:433px;width:183px;height:180px;border:1px solid #ddd;border-radius:5px;box-shadow:0 1px 3px rgba(0,0,0,.12);overflow:hidden}
.cats h2{height:27px;background:var(--blue);color:var(--white);font-family:Delius,cursive;font-weight:400;font-size:12px;padding:7px 0 0 12px}
.cats ul{list-style:none;padding:6px 12px 0}
.cats li{height:24.4px;line-height:23px;border-bottom:1px dashed #e4e4e4;font-size:8.5px;color:var(--blue-link);padding-left:12px;position:relative}
.cats li:last-child{border:0}
.cats li::before{content:"";position:absolute;left:1px;top:9px;border-left:4px solid var(--blue);border-top:3px solid transparent;border-bottom:3px solid transparent}
.service{top:675px;width:212px;height:142px;border:1px solid #ddd;border-radius:4px;background:linear-gradient(#fff,#f2f2f2);box-shadow:0 1px 3px rgba(0,0,0,.15);overflow:hidden}
.service-img{position:absolute;right:0;bottom:0;width:100px;height:122px;border-radius:40px 0 0 0}
.service h3{position:absolute;left:10px;top:10px;font-family:Delius,cursive;font-weight:400;font-size:16px}
.service p{position:absolute;left:10px;top:34px;font-family:Delius,cursive;font-size:13px;line-height:22px;color:#333}
.btn-more{position:absolute;left:10px;top:91px;width:82px;height:24px;border-radius:3px;background:linear-gradient(#fb8f2b,#ef6a0d);border:1px solid #f6b37a;color:var(--white);font-family:Ubuntu,sans-serif;font-size:9.5px;text-align:center;line-height:22px}
.brands-bar{left:74px;top:875px;width:665px;height:60px;background:linear-gradient(#fff,#efefef);border-top:1px solid #e8e8e8;border-radius:4px}
.brand-list{left:95px;top:897px;width:623px;display:flex;justify-content:space-between;font-family:"Black Ops One",sans-serif;font-size:12.5px;color:#333}
.arrow-btn{top:887px;width:17px;height:38px;background:linear-gradient(#4fb2e6,#2a8fcf);border-radius:3px;display:flex;align-items:center;justify-content:center}
.footer{left:75px;top:958px;width:664px;height:242px;background:var(--panel);border-radius:6px 6px 0 0}
.foot-col{top:980px}
.foot-col h4{font-family:Delius,cursive;font-weight:400;font-size:12.5px;color:#333;margin-bottom:8px}
.foot-col p{font-size:8px;line-height:13.5px;color:var(--muted)}
.foot-col ul{list-style:none}
.foot-col li{font-size:8px;color:var(--muted);height:17.6px;padding-left:10px;position:relative}
.foot-col li::before{content:"";position:absolute;left:1px;top:2px;border-left:3px solid #666;border-top:3px solid transparent;border-bottom:3px solid transparent}
.vsep{top:985px;width:0;height:100px;border-left:1px dashed #ddd}
.paytrove{font-family:Delius,cursive;font-size:16px;color:var(--blue);margin:4px 0 6px 30px}
.cards{display:flex;gap:3px;margin:0 0 10px 5px}
.cards span{width:28px;height:17px;border-radius:2px}
.grass{left:0;top:1075px;width:814px;height:125px;background:linear-gradient(180deg,rgba(210,230,150,0) 0,rgba(196,224,120,.55) 55%,#a7d36b 100%)}
.copyright{left:135px;top:1121px;font-size:8px;color:#555}
.copyright a{color:var(--blue-link);text-decoration:none}
</style>
</head>
<body>
<div class="abs top-strip"></div>

<header>
  <div class="abs logo"><span class="logo-dot"></span>Velkor International</div>
  <div class="abs util-links">Wish List (0) &nbsp;|&nbsp; My Account &nbsp;|&nbsp; Shopping Cart &nbsp;|&nbsp; Checkout</div>
  <div class="abs follow">Follow us on:</div>
  <span class="abs social" style="left:637px;background:#3b5998"></span>
  <span class="abs social" style="left:664px;background:#3fb3e6"></span>
  <span class="abs social" style="left:692px;background:#2f7fd0"></span>
  <span class="abs social" style="left:719px;background:#f7931e"></span>
  <div class="abs call">Call Us On: <span>555-014-2290</span></div>
  <div class="abs search">
    <div class="search-field">Search here...</div>
    <svg width="13" height="13" viewBox="0 0 13 13"><circle cx="5.5" cy="5.5" r="4" fill="none" stroke="#fff" stroke-width="2"/><line x1="8.5" y1="8.5" x2="12" y2="12" stroke="#fff" stroke-width="2.2"/></svg>
  </div>
</header>

<nav class="abs nav">
  <div class="abs nav-home" style="top:0"></div>
  <a style="left:119px">Home</a>
  <a style="left:210px">About us</a>
  <a style="left:311px">Products</a>
  <a style="left:410px">Services</a>
  <a style="left:505px">Brands</a>
  <a style="left:588px">Blog</a>
  <a style="left:682px">Contact Us</a>
</nav>

<section class="abs banner-frame"></section>
<div class="abs banner">
  <div class="banner-photo" role="img" aria-label="Photo of three smiling babies playing with soft blocks, a ball and stacking rings"></div>
  <div class="banner-script">Dolorem rum</div>
  <div class="banner-title">Blanditiis voluptater</div>
  <div class="banner-text">Temporibus autem quibusdam et aut officiis aut rerum necessitatibus saepe eveniet</div>
  <div class="btn-shop">Shop Now</div>
  <div class="dots"><i></i><i></i><i></i><i></i><i></i></div>
</div>

<h2 class="abs section-title" style="left:74px;top:428px">Products</h2>
<div class="abs rule" style="left:74px;top:453px;width:462px"></div>
<div class="abs pager">
  <span><svg width="6" height="7"><path d="M5 0 0 3.5 5 7z" fill="#1d5fa6"/></svg></span>
  <span><svg width="6" height="7"><path d="M1 0 6 3.5 1 7z" fill="#1d5fa6"/></svg></span>
</div>

<div class="abs product" style="left:124px">
  <div class="product-img" role="img" aria-label="Stack of baby clothes with a soft doll" style="background:radial-gradient(#f3c9c9,#fff 75%)"></div>
  <h3>Clothes</h3><p>Lorem Ipsum is simply<br>dummy text of the printing</p><div class="add-cart">Add To cart</div>
</div>
<div class="abs product" style="left:244px">
  <div class="product-img" role="img" aria-label="Blue feeding cup, bowl and spoon" style="background:radial-gradient(#7fc4ef,#fff 75%)"></div>
  <h3>Feeding Accessories</h3><p>Lorem Ipsum is simply<br>dummy text of the printing</p><div class="add-cart">Add To cart</div>
</div>
<div class="abs product" style="left:366px">
  <div class="product-img" role="img" aria-label="Pair of soft baby shoes" style="background:radial-gradient(#e8c47a,#fff 75%)"></div>
  <h3>Footwear</h3><p>Lorem Ipsum is simply<br>dummy text of the printing</p><div class="add-cart">Add To cart</div>
</div>
<div class="abs product" style="left:490px">
  <div class="product-img" role="img" aria-label="Soft plush toy" style="background:radial-gradient(#f2d6c8,#fff 75%)"></div>
  <h3>Accessories</h3><p>Lorem Ipsum is simply<br>dummy text of the printing</p><div class="add-cart">Add To cart</div>
</div>

<aside class="abs cats">
  <h2>Product Categories</h2>
  <ul>
    <li>Infant Feeding and Accessories</li>
    <li>Infant Clothing</li>
    <li>Infant Gear</li>
    <li>Maternity Wear</li>
    <li>Mens Underwear</li>
    <li>Homewares and Manchester</li>
  </ul>
</aside>

<h2 class="abs section-title" style="left:75px;top:634px">Our Services</h2>
<div class="abs rule" style="left:75px;top:659px;width:664px"></div>

<div class="abs service" style="left:75px">
  <div class="service-img" role="img" aria-label="Hands holding a glass globe" style="background:linear-gradient(135deg,#cfe6f5,#7fb0d8 60%,#8a6a55)"></div>
  <h3 style="color:var(--red)">Global Sourcing</h3>
  <p>Distribution &amp;<br>Supply Solutions</p>
  <div class="btn-more">More Details</div>
</div>
<div class="abs service" style="left:301px">
  <div class="service-img" role="img" aria-label="Baby sitting with a toy phone" style="background:linear-gradient(135deg,#fff,#f1d8c4 50%,#cfe7c9)"></div>
  <h3 style="color:var(--teal)">Specialist Private</h3>
  <p>Label Manufacturing<br>Facilities</p>
  <div class="btn-more">More Details</div>
</div>
<div class="abs service" style="left:527px">
  <div class="service-img" role="img" aria-label="Baby playing with colourful stacking rings" style="background:linear-gradient(135deg,#fff,#f1d8c4 45%,#b8dcec)"></div>
  <h3 style="color:var(--green)">Strict Quality</h3>
  <p>Assurance Processes<br>&amp; Certifications</p>
  <div class="btn-more">More Details</div>
</div>

<h2 class="abs section-title" style="left:74px;top:834px">Brands</h2>
<div class="abs rule" style="left:74px;top:859px;width:665px"></div>
<div class="abs brands-bar"></div>
<div class="abs arrow-btn" style="left:71px"><svg width="6" height="9"><path d="M5 0 0 4.5 5 9" fill="none" stroke="#fff" stroke-width="2"/></svg></div>
<div class="abs arrow-btn" style="left:725px"><svg width="6" height="9"><path d="M1 0 6 4.5 1 9" fill="none" stroke="#fff" stroke-width="2"/></svg></div>
<div class="abs brand-list">
  <span>Pillowpop</span><span>Tinamorra</span><span>Cradlebloom</span><span>Fenwick Tots</span><span>LinenHarbourRange</span><span>KiteTumble</span>
</div>

<footer>
  <div class="abs footer"></div>
  <div class="abs grass" role="img" aria-label="Illustrated grass, flowers, trees and bees along the bottom edge"></div>
  <div class="abs foot-col" style="left:95px">
    <h4>Information</h4>
    <ul><li>About Us</li><li>Services</li><li>Privacy Policy</li><li>Terms &amp; Condations</li><li>Contact Us</li></ul>
  </div>
  <div class="abs vsep" style="left:200px"></div>
  <div class="abs foot-col" style="left:222px;width:140px">
    <h4>Blog</h4>
    <p>Contrary to popular belief, Lorem Ipsum is not simply random text. It has roots in a piece of classical</p>
    <p style="margin-top:14px">Latin literature from 45 BC, making it over 2000 years old. Richard</p>
  </div>
  <div class="abs vsep" style="left:375px"></div>
  <div class="abs foot-col" style="left:396px;width:140px">
    <h4>Contact Details</h4>
    <p style="line-height:12.5px">Velkor International<br>Lorem Ipsum is simply dummy text of the printing and typesetting</p>
    <p style="margin-top:12px;line-height:12.5px">Tel: 555-014-2290<br>Email: info@velkor-example.com.au</p>
  </div>
  <div class="abs vsep" style="left:549px"></div>
  <div class="abs foot-col" style="left:570px;width:150px">
    <h4>Secure Order Ststem</h4>
    <div class="paytrove">Paytrove</div>
    <div class="cards"><span style="background:#e0442b"></span><span style="background:#1a3d8f"></span><span style="background:#3a8fd0"></span><span style="background:#f0f0f0;border:1px solid #ccc"></span></div>
    <p style="line-height:12.5px">You are safe when you buy with us as we use Paytrove to process all orders.</p>
  </div>
  <div class="abs rule" style="left:95px;top:1100px;width:624px;height:1px"></div>
  <div class="abs copyright">Copyright @ 2010 - 2013 &nbsp;<a>velkor-example.com.au</a> . All Rights Reserved</div>
</footer>
</body>
</html>
```